Re-Design an adult education portal

I need support to re-design an adult education portal. Currently the customer has an incomplete website which should be prepared in a new format.
I have the idea how to realize, but I have no clue how to design it. The hard thing is to have a "beautiful" website with available logo and main color. I hope you can support me.

Name of Website: tovrenu (tovrenu.ch)
Content: adult eduction for adult in safety at work, mountain climbing, dog school. various courses in different areas. But on old webpage is hard to find the different possibilities.
main color: Ral 6011 (green) -> #6C7C59
logo: you see on top of website the logo (2 dogs and a mountain with a colour gradient).

new website: for new webpage I decided to have a navigation for each section of education. In the main area I would like to have some pictures to give an idea what content is behind. At the moment it looks terrible, so I decided to use you as support for me to make the webpage prettier :). And maybe you have an better idea how to make it great. -> current state of new web page: https://tovrenu.bask-om.ch/

Target Market(s)

adult eduction for adult in safety at work, mountain climbing, dog school

Number of Pages Required

1 page

Font styles to use
Serif
Sans Serif

Requirements
Must have
• As main color is set "Ral 6011" (green) -> #6C7C59

```html
<!DOCTYPE html>
<html lang="en">
<head>
<meta charset="utf-8">
<title>tovrenu.ch – Your training and course partner</title>
<link href="https://fonts.googleapis.com/css2?family=Fira+Sans:wght@300;400;500;600;700&display=swap" rel="stylesheet">
<style>
:root{
  --green:#6C7C59;
  --green-nav:#66784f;
  --ring:#94a08a;
  --text:#555;
  --white:#fff;
  --card:#f7f7f6;
  --footer:#0b0b0c;
  --footer-text:#c9c9c9;
}
*{margin:0;padding:0;box-sizing:border-box}
html,body{width:1200px;height:2287px;overflow:hidden}
body{position:relative;font-family:"Fira Sans",sans-serif;background:var(--white);color:var(--text)}
.abs{position:absolute}

/* header */
.site-header{left:0;top:0;width:1200px;height:87px;background:linear-gradient(90deg,#33435a 0%,#46597a 50%,#6685a8 100%)}
.logo-box{left:182px;top:0;width:163px;height:87px;background:#f4f1e2;display:flex;align-items:center;justify-content:center;font-size:27px;font-weight:500;color:#2a2f6a}
.call{right:183px;top:22px;text-align:right;color:var(--white)}
.call small{display:block;font-size:13px;font-weight:500}
.call strong{display:block;font-size:23px;font-weight:500;margin-top:4px}

.main-nav{left:0;top:87px;width:1200px;height:46px;background:var(--green-nav);display:flex;justify-content:center;align-items:center;gap:34px;padding-left:6px}
.main-nav a{color:var(--white);text-decoration:none;font-size:14px;display:flex;align-items:center;gap:5px}
.main-nav svg{width:10px;height:7px}

/* hero */
.hero{left:0;top:133px;width:1200px;height:479px;
  background:
    radial-gradient(ellipse 90px 130px at 64% 62%,rgba(196,160,104,.75),rgba(196,160,104,0) 100%),
    radial-gradient(ellipse 120px 90px at 71% 22%,rgba(205,170,120,.45),rgba(205,170,120,0) 100%),
    radial-gradient(ellipse 180px 240px at 76% 60%,rgba(34,40,34,.75),rgba(34,40,34,0) 100%),
    radial-gradient(ellipse 110px 190px at 30% 45%,rgba(38,44,52,.7),rgba(38,44,52,0) 100%),
    radial-gradient(ellipse 520px 380px at 62% 40%,#5b7a44 0%,rgba(91,122,68,0) 100%),
    linear-gradient(180deg,#4b5a48 0%,#3f4a3c 55%,#54544a 100%)}
.hero-text{left:185px;top:276px;color:var(--white)}
.hero-text h1{font-size:29px;font-weight:700;letter-spacing:-.2px}
.hero-text p{font-size:19px;line-height:41px;margin-top:6px;color:#e6e6e0;width:355px}

/* welcome */
.welcome{left:0;top:612px;width:1200px;height:208px;
  background:
    radial-gradient(ellipse 150px 110px at 66% 40%,rgba(150,118,96,.45),rgba(150,118,96,0) 100%),
    radial-gradient(ellipse 140px 120px at 30% 30%,rgba(140,110,92,.35),rgba(140,110,92,0) 100%),
    radial-gradient(ellipse 160px 140px at 50% 60%,rgba(32,32,30,.5),rgba(32,32,30,0) 100%),
    linear-gradient(90deg,#3c3d3b 0%,#4b4a46 50%,#474844 100%)}
.welcome h2{position:absolute;width:100%;top:62px;text-align:center;color:var(--white);font-size:31px;font-weight:600}

.topic{width:240px;text-align:center}
.topic .ring{width:142px;height:142px;border-radius:50%;background:var(--ring);margin:0 auto;display:flex;align-items:center;justify-content:center}
.topic .photo{width:122px;height:122px;border-radius:50%}
.topic h3{margin-top:17px;font-size:22px;font-weight:500;color:var(--green)}

/* about */
.about-photo{left:183px;top:1017px;width:332px;height:332px;border-radius:50%;
  background:
    radial-gradient(ellipse 60px 40px at 75% 80%,rgba(220,110,70,.8),rgba(220,110,70,0) 100%),
    radial-gradient(ellipse 110px 70px at 45% 82%,rgba(30,30,36,.8),rgba(30,30,36,0) 100%),
    radial-gradient(ellipse 60px 90px at 22% 65%,rgba(200,200,196,.8),rgba(200,200,196,0) 100%),
    radial-gradient(circle at 35% 20%,rgba(200,70,70,.5),rgba(200,70,70,0) 30%),
    radial-gradient(circle at 70% 35%,rgba(70,160,90,.5),rgba(70,160,90,0) 30%),
    linear-gradient(135deg,#5d6ea8 0%,#8088b8 45%,#4a4e66 100%)}
.about-text{left:580px;top:1033px;width:390px}
.about-text h2{font-size:34px;font-weight:600;color:var(--green);line-height:41px}
.about-text p{margin-top:30px;font-size:14px;line-height:21px;color:var(--text);font-weight:300}
.mini-logo{left:580px;top:1262px;width:137px;height:68px;background:#f2efdc;display:flex;align-items:center;justify-content:center;font-size:21px;font-weight:500;color:#2a2f6a}

/* courses */
.courses{left:0;top:1425px;width:1200px;height:544px;
  background:
    radial-gradient(ellipse 200px 260px at 96% 40%,rgba(150,160,140,.35),rgba(150,160,140,0) 100%),
    linear-gradient(180deg,#cfe5dc 0%,#d2e5d4 38%,#c7dccd 42%,#dbe8c8 75%,#d5e6cc 100%)}
.card{width:265px;height:334px;background:var(--card);text-align:center}
.card .icon{width:118px;height:118px;border-radius:50%;margin:33px auto 0}
.card h3{margin-top:30px;font-size:19px;font-weight:500;color:var(--green)}
.card .sub{margin-top:10px;font-size:13px;font-weight:500;color:#555;line-height:26px;min-height:52px}
.card .more{display:block;margin-top:12px;font-size:13px;font-weight:500;color:var(--green);text-decoration:none}
.arrows{left:565px;top:1859px;display:flex;gap:6px}
.arrows span{width:32px;height:32px;border-radius:50%;display:flex;align-items:center;justify-content:center;border:2px solid var(--ring)}
.arrows .prev{background:#c9d1bd}
.arrows .next{background:var(--green)}

/* footer */
.site-footer{left:0;top:1969px;width:1200px;height:318px;background:var(--footer);color:var(--footer-text)}
.foot-logo{left:184px;top:52px;width:103px;height:54px;background:#f2efdc;display:flex;align-items:center;justify-content:center;font-size:16px;font-weight:500;color:#2a2f6a}
.foot-about{left:183px;top:128px;width:205px;font-size:11px;line-height:18px}
.socials{left:183px;top:222px;display:flex;gap:6px}
.socials span{width:16px;height:16px;border-radius:50%;background:var(--white)}
.foot-col h4{font-size:18px;font-weight:400;color:var(--white)}
.foot-col ul{list-style:none;margin-top:30px}
.foot-col li{font-size:12px;line-height:35px}
.contact li{display:flex;align-items:flex-start;gap:16px;font-size:11.5px;line-height:18px;margin-bottom:20px}
.contact .ic{width:22px;height:22px;border-radius:50%;background:#d9d9d9;flex:none;display:flex;align-items:center;justify-content:center}
.contact .ic svg{width:12px;height:12px}
.copy{left:0;width:1200px;text-align:center;font-size:6px;color:#777}
</style>
</head>
<body>

<header class="abs site-header">
  <div class="abs logo-box">tovrenu.ch</div>
  <div class="abs call"><small>Call Us Today</small><strong>+41 79 000 12 34</strong></div>
</header>

<nav class="abs main-nav">
  <a href="#">Occupational Safety <svg viewBox="0 0 10 7"><path d="M1 1l4 4 4-4" fill="none" stroke="#fff" stroke-width="1.3"/></svg></a>
  <a href="#">First Aid <svg viewBox="0 0 10 7"><path d="M1 1l4 4 4-4" fill="none" stroke="#fff" stroke-width="1.3"/></svg></a>
  <a href="#">Dog School <svg viewBox="0 0 10 7"><path d="M1 1l4 4 4-4" fill="none" stroke="#fff" stroke-width="1.3"/></svg></a>
  <a href="#">Mountain Clumbling <svg viewBox="0 0 10 7"><path d="M1 1l4 4 4-4" fill="none" stroke="#fff" stroke-width="1.3"/></svg></a>
  <a href="#">CZV <svg viewBox="0 0 10 7"><path d="M1 1l4 4 4-4" fill="none" stroke="#fff" stroke-width="1.3"/></svg></a>
</nav>

<section class="abs hero" role="img" aria-label="Hikers on a rocky mountain trail and a woman kneeling with a labrador, under a green tint"></section>
<div class="abs hero-text">
  <h1>YOUR TRAINING AND COURSE PARTNER</h1>
  <p>We offer training tailored to your needs, target-oriented and tailored to your skills and knowledge.</p>
</div>

<section class="abs welcome" role="img" aria-label="Group of laughing adults outdoors, darkened backdrop">
  <h2>Welcome to Adult Eduction</h2>
</section>

<div class="abs topic" style="left:193px;top:756px">
  <div class="ring"><div class="photo" role="img" aria-label="Hiker with a large backpack in the mist" style="background:radial-gradient(ellipse 34px 50px at 58% 62%,#2f3a42 0%,rgba(47,58,66,0) 100%),radial-gradient(ellipse 24px 40px at 38% 62%,#3b4a56 0%,rgba(59,74,86,0) 100%),linear-gradient(160deg,#a9c7d2 0%,#7fa0ae 55%,#5a7482 100%)"></div></div>
  <h3>ADULT IN SAFETY</h3>
</div>
<div class="abs topic" style="left:479px;top:756px">
  <div class="ring"><div class="photo" role="img" aria-label="Climber with helmet on a rock face" style="background:radial-gradient(ellipse 22px 50px at 52% 55%,#2a2826 0%,rgba(42,40,38,0) 100%),radial-gradient(ellipse 16px 26px at 52% 80%,rgba(150,110,90,.8),rgba(150,110,90,0) 100%),linear-gradient(160deg,#9a958e 0%,#7a746c 50%,#55504a 100%)"></div></div>
  <h3>MOUNTAIN CLIMBING</h3>
</div>
<div class="abs topic" style="left:764px;top:756px">
  <div class="ring"><div class="photo" role="img" aria-label="Corgi on a wooden jetty by a lake" style="background:radial-gradient(ellipse 26px 38px at 50% 48%,#d99a5a 0%,rgba(217,154,90,0) 100%),linear-gradient(180deg,#4f8fd0 0%,#7fb0de 32%,#9d8a6e 55%,#b8a588 80%,#7d6c58 100%)"></div></div>
  <h3>DOG SCHOOL</h3>
</div>

<div class="abs about-photo" role="img" aria-label="Woman resting in front of an indoor climbing wall with coloured holds"></div>
<div class="abs about-text">
  <h2>When You Need Batter Option</h2>
  <p>Elevating work platforms are an efficient work tool. Operators have to be carefully selected and require specific training. The employer is responsible for the selection and training of the people who carry out this work.</p>
</div>
<div class="abs mini-logo">tovrenu.ch</div>

<section class="abs courses" role="img" aria-label="Pale green seaside scene with a figure on the beach"></section>

<article class="abs card" style="left:183px;top:1493px">
  <div class="icon" role="img" aria-label="Red forklift" style="background:radial-gradient(ellipse 40px 22px at 50% 62%,#d4302a 0%,rgba(212,48,42,0) 100%),radial-gradient(ellipse 46px 40px at 45% 48%,#2b2b2b 0%,rgba(43,43,43,0) 100%),#f4f4f4"></div>
  <h3>FORKLIFT COURSES</h3>
  <div class="sub">BASIC TRAINING</div>
  <a class="more" href="#">READ MORE</a>
</article>
<article class="abs card" style="left:468px;top:1497px">
  <div class="icon" role="img" aria-label="Coiled red, blue and yellow safety ropes" style="background:radial-gradient(ellipse 22px 26px at 38% 50%,rgba(190,60,50,.85),rgba(190,60,50,0) 100%),radial-gradient(ellipse 22px 26px at 62% 52%,rgba(60,80,160,.7),rgba(60,80,160,0) 100%),radial-gradient(ellipse 14px 30px at 72% 30%,rgba(210,170,60,.7),rgba(210,170,60,0) 100%),#e2ddd5"></div>
  <h3>PPE</h3>
  <div class="sub">PERSÖNLICHE&nbsp; SCHUTZAUSRÜSTUNG<br>GEGEN ABSTURZ (PSAGA)</div>
  <a class="more" href="#">READ MORE</a>
</article>
<article class="abs card" style="left:753px;top:1497px">
  <div class="icon" role="img" aria-label="Orange elevating work platform in a mountain valley" style="background:radial-gradient(ellipse 30px 14px at 65% 72%,rgba(230,110,40,.85),rgba(230,110,40,0) 100%),radial-gradient(ellipse 22px 34px at 18% 70%,rgba(90,70,50,.8),rgba(90,70,50,0) 100%),linear-gradient(180deg,#6e9fd6 0%,#a9c3de 30%,#7f8a78 50%,#8c8c84 72%,#5e5e58 100%)"></div>
  <h3>HUBARBEITSBÜHNE</h3>
  <div class="sub">BEDIENERSCHULUNG<br>BEDIENERSCHULUNG / CZV</div>
  <a class="more" href="#">READ MORE</a>
</article>

<div class="abs arrows">
  <span class="prev"><svg width="10" height="12" viewBox="0 0 10 12"><path d="M7 1L2 6l5 5" fill="none" stroke="#6b6b6b" stroke-width="1.4"/></svg></span>
  <span class="next"><svg width="10" height="12" viewBox="0 0 10 12"><path d="M3 1l5 5-5 5" fill="none" stroke="#fff" stroke-width="1.4"/></svg></span>
</div>

<footer class="abs site-footer">
  <div class="abs foot-logo">tovrenu.ch</div>
  <p class="abs foot-about">Your training and course partner<br>We offer training tailored to your needs , target-oriented and tailored to your skills and knowledge .</p>
  <div class="abs socials"><span></span><span></span><span></span></div>

  <div class="abs foot-col" style="left:421px;top:66px">
    <h4>Sitemap</h4>
    <ul><li>safety at work</li><li>mountain climbing</li><li>dog school</li></ul>
  </div>
  <div class="abs foot-col" style="left:598px;top:66px">
    <h4>Useful links</h4>
    <ul><li>Team</li><li>Terms and Conditions</li><li>Certificates</li></ul>
  </div>
  <div class="abs foot-col" style="left:802px;top:66px">
    <h4>Get in Touch</h4>
    <ul class="contact" style="margin-top:24px">
      <li><span class="ic"><svg viewBox="0 0 12 12"><path d="M6 1a3.5 3.5 0 0 0-3.5 3.5C2.5 7 6 11 6 11s3.5-4 3.5-6.5A3.5 3.5 0 0 0 6 1z" fill="#555"/><circle cx="6" cy="4.5" r="1.2" fill="#d9d9d9"/></svg></span>Talweg 27, CH-3900<br>Brig</li>
      <li><span class="ic"><svg viewBox="0 0 12 12"><path d="M3 1.5l2 2-1 1.3a6 6 0 0 0 3.2 3.2l1.3-1 2 2-1.2 1.5C5.5 10.5 1.5 6.5 1.5 2.7z" fill="#555"/></svg></span>+41 79 000 12 34</li>
      <li><span class="ic"><svg viewBox="0 0 12 12"><rect x="1.5" y="3" width="9" height="6.5" fill="none" stroke="#555" stroke-width="1"/><path d="M1.5 3.5L6 7l4.5-3.5" fill="none" stroke="#555" stroke-width="1"/></svg></span>info@tovrenu.ch</li>
    </ul>
  </div>
  <p class="abs copy" style="top:298px">©tovrenu.ch , All right Reserved</p>
</footer>

</body>
</html>
```